New Advertising Company Business Card

A two sided business card. One side with logo only and the other side with my information and maybe my logo again. Looking for something unique and creative, but not too busy. Info would include my name(Marcus Feldon), President, phone number, address, email address, and website. LOGO IS THE BLUE AND WHITE ONE.

Target Market(s)

CEO/VP Level Audience

Industry/Entity Type

Business

Contact Information for Business Card

In Description.

```html
<!DOCTYPE html>
<html lang="en">
<head>
<meta charset="UTF-8">
<title>Lumen Advertising — Business Card</title>
<link href="https://fonts.googleapis.com/css2?family=Open+Sans:wght@400;600;700&display=swap" rel="stylesheet">
<style>
  :root {
    --backdrop: #c8b29a;
    --card: #ffffff;
    --brand-blue: #1a6fc4;
    --ink: #2b2b2b;
    --muted: #555555;
  }
  * { margin: 0; padding: 0; box-sizing: border-box; }
  html, body {
    width: 1200px; height: 1200px; overflow: hidden;
    background: var(--backdrop);
    font-family: "Open Sans", Arial, sans-serif;
  }
  .sheet {
    width: 1200px; height: 1200px;
    display: flex; flex-direction: column; align-items: center; justify-content: center;
    gap: 60px;
  }
  .card {
    position: relative;
    width: 840px; height: 480px;
    background: var(--card);
    box-shadow: 0 6px 18px rgba(60, 40, 20, 0.18);
  }
  .card__rule {
    position: absolute; left: 0; right: 0; top: 62px;
    height: 3px; background: var(--brand-blue);
  }
  .wordmark {
    display: flex; align-items: center; gap: 12px;
    color: var(--brand-blue);
    font-weight: 600; letter-spacing: 0.14em; text-transform: uppercase;
  }
  .wordmark__dot {
    width: 18px; height: 18px; border-radius: 50%;
    background: var(--brand-blue);
  }
  /* info side */
  .person { position: absolute; left: 60px; top: 88px; }
  .person__name {
    color: var(--brand-blue); font-weight: 700; font-size: 32px;
    text-transform: uppercase; letter-spacing: 0.01em; line-height: 1.1;
  }
  .person__title { color: var(--ink); font-size: 22px; margin-top: 2px; }
  .contacts {
    position: absolute; left: 60px; top: 250px;
    list-style: none; color: var(--brand-blue); font-size: 19px; line-height: 1.35;
  }
  .contacts li { display: flex; align-items: flex-start; gap: 14px; margin-bottom: 8px; }
  .contacts svg { width: 18px; height: 18px; flex: none; margin-top: 4px; fill: var(--brand-blue); }
  .card--info .wordmark { position: absolute; right: 60px; bottom: 56px; font-size: 28px; }
  /* logo side */
  .card--logo .wordmark { position: absolute; left: 60px; top: 100px; font-size: 34px; }
  .website {
    position: absolute; right: 60px; top: 84px;
    color: var(--muted); font-size: 18px;
  }
</style>
</head>
<body>
<main class="sheet">

  <section class="card card--info" aria-label="Business card, contact side">
    <div class="card__rule"></div>
    <div class="person">
      <h1 class="person__name">Marcus Feldon</h1>
      <p class="person__title">President</p>
    </div>
    <ul class="contacts">
      <li>
        <svg viewBox="0 0 24 24" aria-hidden="true"><path d="M6.6 10.8a15.1 15.1 0 0 0 6.6 6.6l2.2-2.2a1 1 0 0 1 1-.25 11.4 11.4 0 0 0 3.6.57 1 1 0 0 1 1 1V20a1 1 0 0 1-1 1A17 17 0 0 1 3 4a1 1 0 0 1 1-1h3.5a1 1 0 0 1 1 1c0 1.25.2 2.45.57 3.6a1 1 0 0 1-.25 1z"/></svg>
        <span>555-014-229</span>
      </li>
      <li>
        <svg viewBox="0 0 24 24" aria-hidden="true"><path d="M3 5h18a1 1 0 0 1 1 1v12a1 1 0 0 1-1 1H3a1 1 0 0 1-1-1V6a1 1 0 0 1 1-1zm9 7.2L20 7H4zM4 9v8h16V9l-8 5.2z"/></svg>
        <span>info@lumenadvertising.com</span>
      </li>
      <li>
        <svg viewBox="0 0 24 24" aria-hidden="true"><path d="M12 2a7 7 0 0 0-7 7c0 5.2 7 13 7 13s7-7.8 7-13a7 7 0 0 0-7-7zm0 9.5A2.5 2.5 0 1 1 12 6.5a2.5 2.5 0 0 1 0 5z"/></svg>
        <span>27 Maren Ave.<br>Alder Bay, HI 96702</span>
      </li>
    </ul>
    <div class="wordmark"><span class="wordmark__dot"></span><span>Lumen Advertising</span></div>
  </section>

  <section class="card card--logo" aria-label="Business card, logo side">
    <div class="card__rule"></div>
    <div class="wordmark"><span class="wordmark__dot"></span><span>Lumen Advertising</span></div>
    <p class="website">www.lumenadvertising.com</p>
  </section>

</main>
</body>
</html>
```